Business Card Design Project

I need a cool business card design for the company that will build residential houses.
The card should include:
1) Name: Boris Kalinov
2) Cell: 587.204.XXXX
3) Email: bor.kalinov@qwvend.example
4) Position: General Manager
5) Residential Home Building
6) Company logo that I have uploaded

Industry/Entity Type

Residential

```html
<!DOCTYPE html>
<html lang="en">
<head>
<meta charset="utf-8">
<title>Qwvend Developments – Business Card</title>
<link href="https://fonts.googleapis.com/css2?family=Didact+Gothic&family=Open+Sans:wght@400;600;700&display=swap" rel="stylesheet">
<style>
  :root {
    --bg: #e9ebee;
    --card: #fbfcfd;
    --blue: #1c4fa0;
    --blue-dark: #173f8c;
    --green: #5aab2e;
    --grey-text: #8a8d91;
    --ink: #2b2b2b;
    --shadow: 0 10px 24px rgba(40, 50, 70, 0.18);
  }
  * { box-sizing: border-box; margin: 0; padding: 0; }
  html, body { width: 1200px; height: 843px; overflow: hidden; }
  body {
    background: var(--bg);
    font-family: "Open Sans", Arial, sans-serif;
    display: flex;
    align-items: center;
    justify-content: center;
    gap: 40px;
  }
  .card {
    position: relative;
    width: 540px;
    height: 309px;
    background: var(--card);
    box-shadow: var(--shadow);
    overflow: hidden;
  }
  .brand {
    position: absolute;
    display: flex;
    align-items: center;
    gap: 10px;
    color: var(--blue);
    font-family: "Didact Gothic", "Century Gothic", sans-serif;
    font-weight: 400;
    font-size: 27px;
    line-height: 1.05;
  }
  .brand-dot {
    width: 34px; height: 34px;
    border-radius: 50%;
    background: var(--green);
    flex: none;
  }
  /* back side */
  .card-back .brand { left: 60px; top: 70px; }
  .card-back .swoosh { position: absolute; left: 0; bottom: 0; width: 540px; height: 150px; }
  /* front side */
  .card-front .brand { left: 34px; top: 80px; font-size: 24px; }
  .tagline {
    position: absolute;
    left: 120px; top: 168px;
    color: var(--grey-text);
    font-family: "Didact Gothic", "Century Gothic", sans-serif;
    font-size: 21px;
    line-height: 1.2;
    text-align: center;
  }
  .person { position: absolute; left: 300px; top: 70px; }
  .person-name { font-weight: 700; font-size: 15px; letter-spacing: 0.5px; color: var(--ink); text-transform: uppercase; }
  .person-role { font-size: 11.5px; color: var(--ink); margin-top: 1px; padding-left: 8px; }
  .contact { position: absolute; left: 300px; top: 152px; font-size: 11.5px; color: var(--ink); line-height: 1.45; }
  .contact-label { color: var(--blue); font-weight: 700; }
  .strip { position: absolute; bottom: 0; height: 14px; }
  .strip-blue { left: 0; width: 62%; background: linear-gradient(90deg, var(--blue-dark), var(--blue)); }
  .strip-green { right: 0; width: calc(38% - 4px); background: var(--green); }
</style>
</head>
<body>
  <section class="card card-back" aria-label="Card back">
    <div class="brand"><span class="brand-dot"></span><span>Qwvend<br>Developments</span></div>
    <svg class="swoosh" viewBox="0 0 540 150" preserveAspectRatio="none" aria-hidden="true">
      <path d="M0 72 C160 70 360 40 540 0 L540 150 L0 150 Z" fill="var(--green)"/>
      <path d="M0 77 C160 75 360 46 540 6 L540 150 L0 150 Z" fill="var(--card)"/>
      <path d="M0 82 C160 80 360 52 540 12 L540 150 L0 150 Z" fill="var(--blue)"/>
    </svg>
  </section>

  <section class="card card-front" aria-label="Card front">
    <div class="brand"><span class="brand-dot"></span><span>Qwvend<br>Developments</span></div>
    <p class="tagline">Residential<br>Home Building</p>
    <div class="person">
      <p class="person-name">Boris Kalinov</p>
      <p class="person-role">General Manager</p>
    </div>
    <div class="contact">
      <p><span class="contact-label">Cell:</span> 587.204.XXXX</p>
      <p><span class="contact-label">Email:</span> bor.kalinov@qwvend.example</p>
    </div>
    <div class="strip strip-blue"></div>
    <div class="strip strip-green"></div>
  </section>
</body>
</html>
```